Dravetti Business Cards

We need a business card design for Dravetti Mining.

This is a B2B company that buys and sells large machinery tires within the coal mining industry. The design should the strong, crisp and masculine. I have uploaded the company logo and rough mock-up of what the back of the card should look like. the front of the card should have the same look/feel as the back. I need editable templates for both the front and the back of the card.

Color scheme should be grey/green/black

Contact information to include on the card:
Name: Owen Pellsworth
Title: Managing Director
Phone: 972-555-0143
Address: 3157 Brantley #5 Dallas, TX 75209
Email: Owen@Dravetti-example.com

I am also opening a contest for letterhead design. If you submit a business card design, please also submit a letterhead design with the same look/feel. The winner of the business card design will also will the letter head and be paid for both.

Target Market(s)

Procurement men/women in the coal mining industry

Industry/Entity Type

Coal Mining

```html
<!DOCTYPE html>
<html lang="en">
<head>
<meta charset="utf-8">
<title>Dravetti Business Cards</title>
<link rel="stylesheet" href="https://fonts.googleapis.com/css2?family=Open+Sans:wght@400;600;700&display=swap">
<style>
  :root {
    --backdrop: #e4e2df;
    --card-white: #f7f7f7;
    --card-black: #2a2a2a;
    --strip-dark: #2b2b2b;
    --brand-green: #5aab2e;
    --brand-grey: #5f6163;
    --text-dark: #2f2f2f;
    --text-light: #f2f2f2;
  }
  * { margin: 0; padding: 0; box-sizing: border-box; }
  html, body { width: 1200px; height: 900px; overflow: hidden; }
  body {
    position: relative;
    background: var(--backdrop);
    font-family: "Open Sans", Arial, sans-serif;
  }
  .card {
    position: absolute;
    left: 353px;
    width: 490px;
    height: 280px;
    box-shadow: 0 3px 8px rgba(0,0,0,0.25);
  }
  .card-front { top: 160px; background: var(--card-white); }
  .card-back { top: 470px; background: var(--card-black); }

  .side-strip {
    position: absolute; left: 0; top: 0;
    width: 45px; height: 100%;
    background: var(--strip-dark);
    border-right: 5px solid var(--brand-green);
  }
  .side-strip .website {
    position: absolute;
    left: 28px; top: 70px;
    transform: rotate(90deg);
    transform-origin: left top;
    color: var(--text-light);
    font-size: 13px;
    letter-spacing: 0.6px;
    white-space: nowrap;
  }
  .brand {
    position: absolute;
    display: flex; align-items: center; gap: 12px;
    font-weight: 700;
    letter-spacing: 1px;
    white-space: nowrap;
  }
  .brand .brand-square {
    width: 32px; height: 32px;
    background: var(--brand-green);
  }
  .card-front .brand { right: 28px; top: 52px; font-size: 30px; color: var(--brand-grey); }
  .card-back .brand { left: 70px; top: 114px; font-size: 30px; color: var(--text-light); }

  .contact {
    position: absolute; top: 212px;
    font-size: 11.5px; line-height: 21px;
    color: var(--text-dark);
    white-space: nowrap;
  }
  .contact-person { left: 64px; }
  .contact-person .name { font-weight: 700; font-size: 12.5px; }
  .contact-person .title { font-size: 10px; text-transform: uppercase; }
  .contact-lines { left: 186px; }
  .contact-lines .line { display: flex; align-items: center; gap: 6px; }
  .contact-lines svg { width: 10px; height: 10px; fill: var(--brand-green); flex: none; }
  .contact-address { right: 18px; }
</style>
</head>
<body>
  <section class="card card-front">
    <div class="side-strip"><span class="website">www.Dravetti-example.com</span></div>
    <div class="brand"><span class="brand-square"></span>DRAVETTI MINING</div>
    <div class="contact contact-person">
      <div class="name">Owen Pellsworth</div>
      <div class="title">Managing Director</div>
    </div>
    <div class="contact contact-lines">
      <div class="line">
        <svg viewBox="0 0 24 24" aria-hidden="true"><path d="M6.6 10.8a15.1 15.1 0 0 0 6.6 6.6l2.2-2.2a1 1 0 0 1 1-.25 11.4 11.4 0 0 0 3.6.57 1 1 0 0 1 1 1V20a1 1 0 0 1-1 1A17 17 0 0 1 3 4a1 1 0 0 1 1-1h3.5a1 1 0 0 1 1 1c0 1.250.2 2.450.57 3.57a1 1 0 0 1-.25 1z"/></svg>
        <span>972-555-0143</span>
      </div>
      <div class="line">
        <svg viewBox="0 0 24 24" aria-hidden="true"><path d="M2 6h20v12H2z M2 6l10 7 10-7" fill="none" stroke="#5aab2e" stroke-width="2.5"/></svg>
        <span>Owen@Dravetti-example.com</span>
      </div>
    </div>
    <div class="contact contact-address">
      <div>3157 Brantley #5</div>
      <div>Dallas, TX 75209</div>
    </div>
  </section>

  <section class="card card-back">
    <div class="brand"><span class="brand-square"></span>DRAVETTI MINING</div>
  </section>
</body>
</html>
```